Merrow Consulting needs a business card design

Merrow Consulting is a small business that consults and trains Australia wide in Workplace Health and Safety, Environment and Quality Management Systems.

Clients are typically smaller businesses with 50 to 200 employees but there are some large clients.

Communication is often by email, although mobile is used as well.

Merrow Consulting
41 Tulwin Ferris Road
Ardlow Vale, QLD 4312
0438 291 064

```html
<!DOCTYPE html>
<html lang="en">
<head>
<meta charset="utf-8">
<title>Merrow Consulting – Business Card</title>
<link href="https://fonts.googleapis.com/css2?family=Questrial&family=Montserrat:wght@700&display=swap" rel="stylesheet">
<style>
  :root {
    --page-bg: #e9eaeb;
    --card-dark: #2f2f31;
    --card-light: #f7f8f9;
    --brand-blue: #1f6f95;
    --text-grey: #5a5d61;
    --text-light: #e6e6e6;
  }
  * { margin: 0; padding: 0; box-sizing: border-box; }
  html, body {
    width: 1200px;
    height: 898px;
    overflow: hidden;
    background: var(--page-bg);
    font-family: "Questrial", sans-serif;
  }
  .card-set {
    position: relative;
    width: 1200px;
    height: 898px;
  }
  .card {
    position: absolute;
    top: 284px;
    width: 540px;
    height: 330px;
    box-shadow: 0 6px 18px rgba(0, 0, 0, 0.18);
  }
  .card--back {
    left: 40px;
    background: var(--card-dark);
    display: flex;
    align-items: center;
    justify-content: center;
  }
  .card--front {
    left: 620px;
    background: var(--card-light);
  }
  .wordmark {
    font-family: "Questrial", sans-serif;
    font-size: 25px;
    letter-spacing: 1px;
    text-transform: uppercase;
    white-space: nowrap;
  }
  .card--back .wordmark { color: var(--text-light); }
  .card--front .wordmark {
    position: absolute;
    top: 56px;
    right: 40px;
    color: var(--brand-blue);
  }
  .accent-square {
    position: absolute;
    left: 0;
    top: 76px;
    width: 17px;
    height: 17px;
    background: var(--brand-blue);
  }
  .website {
    position: absolute;
    top: 90px;
    right: 40px;
    font-size: 12px;
    letter-spacing: 0.6px;
    color: var(--text-grey);
  }
  .holder-name {
    position: absolute;
    left: 40px;
    bottom: 44px;
    font-family: "Montserrat", sans-serif;
    font-weight: 700;
    font-size: 17px;
    letter-spacing: 0.5px;
    color: var(--text-grey);
    text-transform: uppercase;
  }
  .contact {
    position: absolute;
    right: 40px;
    bottom: 44px;
    text-align: right;
    font-style: normal;
    font-size: 11.5px;
    line-height: 1.45;
    letter-spacing: 0.4px;
    color: var(--text-grey);
    white-space: nowrap;
  }
  .contact .label {
    color: var(--brand-blue);
    font-weight: 700;
  }
</style>
</head>
<body>
  <main class="card-set">
    <section class="card card--back" aria-label="Card back">
      <span class="wordmark">Merrow Consulting</span>
    </section>

    <section class="card card--front" aria-label="Card front">
      <span class="accent-square"></span>
      <span class="wordmark">Merrow Consulting</span>
      <span class="website">www.merrowconsulting.com</span>
      <span class="holder-name">Dean Merrow</span>
      <address class="contact">
        <span class="label">T:</span> 0438 291 064 · <span class="label">E:</span> d.merrow@mailbox.com<br>
        41 Tulwin Ferris Road, Ardlow Vale, QLD 4312
      </address>
    </section>
  </main>
</body>
</html>
```